Mezzanine Floor Manufacturer looking for a new business card design

We manufacture mezzanine floors and are providers of racking systems. We provide a range of items/services - simple rack repairs , full warehouse fit outs , manufacturer and install mezzanine floors , partitioning and large turnkey projects. Recently had a new website - www.corvane-shelving.co.uk and would like our business cards updating aswell . Our current card is single sided in the old logo colours (pdf attached) and needs updating.

Target Market(s)

We deal with large projects/ multi national companies and also smaller projects and companies throughout the UK ranging from a single warehouse to a large multi site company.

Industry/Entity Type

Business

Contact Information for Business Card

Will have job title,tel no's, email ,website address etc like example pdf

Requirements
Must have
• Hi - needs to use the colours of the logo & new website. Card needs to be professional

```html
<!DOCTYPE html>
<html lang="en">
<head>
<meta charset="utf-8">
<title>Corvane Business Cards</title>
<link href="https://fonts.googleapis.com/css2?family=Arvo:wght@700&family=Arimo:ital,wght@0,400;1,400&family=Tinos&display=swap" rel="stylesheet">
<style>
  :root{
    --backdrop:#2b211b;
    --card-black:#0a0a0a;
    --plate-dark:#1c1c1c;
    --plate-light:#3a3b3c;
    --brand-red:#c8141a;
    --brand-red-dark:#8c0c10;
    --white:#ffffff;
    --silver-light:#f2f2f2;
    --silver-mid:#9a9a9a;
    --silver-dark:#4a4a4a;
  }
  *{margin:0;padding:0;box-sizing:border-box}
  html,body{width:1200px;height:1200px;overflow:hidden;background:var(--backdrop)}
  .canvas{position:relative;width:1200px;height:1200px}
  .card{position:absolute;overflow:hidden;box-shadow:0 8px 20px rgba(0,0,0,.55)}
  .text{position:absolute;color:var(--white);white-space:nowrap}
  .sans{font-family:"Arimo",Arial,sans-serif}
  .serif{font-family:"Tinos","Times New Roman",serif}
  .brand-name{font-family:"Arvo",Georgia,serif;font-weight:700;color:var(--white)}
  .brand-dot{position:absolute;border-radius:50%;background:radial-gradient(circle at 40% 35%,var(--brand-red),var(--brand-red-dark))}

  /* Back card: contact details */
  .card-back{left:98px;top:164px;width:784px;height:452px;background:var(--card-black)}
  .plate-panel{position:absolute;left:0;top:0;width:372px;height:452px;
    background:radial-gradient(ellipse at 80% 60%,var(--plate-light),var(--plate-dark) 70%)}
  .panel-divider{position:absolute;left:372px;top:0;width:4px;height:452px;
    background:linear-gradient(var(--silver-dark),var(--silver-mid),var(--silver-dark))}
  .centered{left:0;width:372px;text-align:center}
  .card-back .brand-dot{left:124px;top:56px;width:90px;height:90px}
  .card-back .brand-name{top:180px;font-size:36px}
  .person-name{top:258px;font-size:28px}
  .job-title{top:297px;font-size:20px;font-style:italic}
  .mobile{top:324px;font-size:23px;letter-spacing:.5px}
  .tel{top:365px;font-size:23px;letter-spacing:.5px}
  .fax{top:391px;font-size:23px;letter-spacing:.5px}
  .service-list{position:absolute;left:394px;top:43px;list-style:none}
  .service-list li{position:relative;padding-left:22px;height:25.3px;font-family:"Arimo",Arial,sans-serif;font-size:21px;color:var(--white);line-height:25px}
  .service-list li::before{content:"";position:absolute;left:0;top:6px;width:14px;height:14px;border-radius:50%;
    background:radial-gradient(circle at 45% 40%,var(--white),var(--silver-mid) 55%,var(--silver-dark))}
  .address{left:394px;top:265px;font-size:19px;line-height:27px;letter-spacing:.4px}
  .web-block{left:394px;top:365px;font-size:19px;line-height:27px;letter-spacing:.4px}

  /* Front card: brand face */
  .card-front{left:318px;top:646px;width:784px;height:454px;
    background:radial-gradient(ellipse at 50% 45%,#222,var(--card-black) 75%)}
  .silver-band{position:absolute;left:0;width:784px;height:19px;
    background:linear-gradient(90deg,var(--silver-dark),var(--silver-light) 28%,var(--silver-mid) 45%,var(--silver-light) 72%,var(--silver-dark))}
  .band-top{top:0}
  .band-bottom{bottom:0}
  .front-center{left:0;width:784px;text-align:center}
  .card-front .brand-dot{left:322px;top:110px;width:140px;height:140px}
  .card-front .brand-name{top:258px;font-size:46px}
  .front-contact{top:320px;font-size:19px;line-height:24px;letter-spacing:.4px}
</style>
</head>
<body>
<div class="canvas">

  <section class="card card-back" aria-label="Business card, contact side">
    <div class="plate-panel" role="img" aria-label="Steel diamond tread plate texture"></div>
    <div class="panel-divider"></div>

    <div class="brand-dot"></div>
    <div class="text brand-name centered">Corvane</div>
    <div class="text sans person-name centered">DANIEL FENWICK</div>
    <div class="text sans job-title centered">TECHNICAL SALES</div>
    <div class="text serif mobile centered">07700 900418</div>
    <div class="text serif tel centered"><span class="sans">Tel:</span> 01632 960748</div>
    <div class="text serif fax centered"><span class="sans">Fax:</span> 01632 960998</div>

    <ul class="service-list">
      <li>MEZZANINE FLOORS</li>
      <li>CANTILEVER RACKING</li>
      <li>PALLET RACKING</li>
      <li>SAFETY BARRIERS</li>
      <li>LONGSAPAN SHELVING</li>
      <li>STEEL SHELVING</li>
      <li>PARTITIONING</li>
      <li>TURNKEY PROJECTS</li>
    </ul>

    <div class="text sans address">Millbrook Close<br>Ashcroft Business Park<br>Holtby, Derbyshire DE9 4QL</div>
    <div class="text sans web-block">sales@www.corvane-shelving.co.uk<br>www.www.corvane-shelving.co.uk</div>
  </section>

  <section class="card card-front" aria-label="Business card, brand side">
    <div class="silver-band band-top"></div>
    <div class="brand-dot"></div>
    <div class="text brand-name front-center">Corvane</div>
    <div class="text sans front-contact front-center">sales@www.corvane-shelving.co.uk<br>www.www.corvane-shelving.co.uk</div>
    <div class="silver-band band-bottom"></div>
  </section>

</div>
</body>
</html>
```